A Cool Business Card so My Son can Network with People, Especially People in the Entertainment Business. Something that stands out and;Pops:*) He's an Entertainer goes by the ☆Copper Wave CW Please include His Social Media that you will see and Contact Numbers as well in the pics. Submitted Please Hook It Up. Thanks!

Contact Information for Business Card:

A Cool Hip-hop ,Entertainer Design for My 16 Year old Son. He Sings,Raps,Actor,Dancer and Radio Personality as well. Something that stands out from the rest of the Business Cards & Pops. He's A Star Already it's only a matter of Time Until He Becomes A Superstar.

Thank You For Your Help!

Target Market(s)

18-40 y/o

Industry/Entity Type

Entertainment Industry

Contact Information for Business Card

To promote my artistry to the public
Im a Singer,Rapper,Dancer,Actor&Model

Font styles to use
Serif

Requirements
Must have
• artist name- Copper Wave CW
• social media connections
• which are on the pics. downloaded.
Nice to have
• *Copper Wave* CW
• Social Media Info as well as cell phone info located in downloads:*}
• Make it pop,add some of the Pics. Be Creative He is a Future Superstar:*)
Should not have
• Make it Amazing But also readable for His important info But make the Card off the chain any colors dont make it Girly He is a 16 year old Teenager. I left enough downloads of Pics. that someone who is Creative can make something Wonderful. Then whoever that is will work with Us on other Projects Including makin a CD Cover:.)

```html
<!DOCTYPE html>
<html lang="en">
<head>
<meta charset="utf-8">
<title>Copper Wave CW – Business Card</title>
<link rel="stylesheet" href="https://fonts.googleapis.com/css2?family=Open+Sans:wght@400;600&display=swap">
<style>
  :root {
    --page-bg: #e4e4e4;
    --card-white: #fbfbfb;
    --ink-black: #0c0c0c;
    --ink-dark: #1a1a1a;
    --text-light: #f2f2f2;
    --photo-top: #3a3a3a;
    --photo-bottom: #151515;
    --social-orange: #f39a21;
    --social-blue: #3b6fa0;
    --social-red: #d6322c;
  }
  * { margin: 0; padding: 0; box-sizing: border-box; }
  html, body {
    width: 1200px; height: 720px; overflow: hidden;
    background: var(--page-bg);
    font-family: "Open Sans", sans-serif;
  }
  .canvas { position: relative; width: 1200px; height: 720px; }

  .card {
    position: absolute; top: 240px;
    width: 420px; height: 240px;
    background: var(--card-white);
    overflow: hidden;
  }
  .card--front { left: 147px; }
  .card--back { left: 633px; }

  /* Front */
  .band-top {
    position: absolute; left: 0; top: 0;
    width: 180px; height: 120px;
    background: var(--ink-black);
  }
  .band-bottom {
    position: absolute; right: 0; bottom: 0;
    width: 190px; height: 120px;
    background: var(--ink-black);
  }
  .portrait {
    position: absolute; left: 88px; top: 0;
    width: 152px; height: 240px;
    background: linear-gradient(180deg, var(--photo-top), var(--photo-bottom));
  }
  .brand-name {
    position: absolute;
    font-weight: 600;
    letter-spacing: 0.06em;
    text-transform: uppercase;
  }
  .card--front .brand-name {
    left: 22px; top: 56px;
    font-size: 11px;
    color: var(--text-light);
  }

  .socials {
    position: absolute; right: 21px; top: 34px;
    list-style: none;
  }
  .socials li {
    display: flex; align-items: center; justify-content: flex-end;
    height: 19.2px;
    font-size: 10.5px; color: var(--ink-dark);
    letter-spacing: 0.03em;
  }
  .socials .dot {
    display: inline-block; width: 13px; height: 13px;
    margin-left: 7px; border-radius: 2px;
  }
  .dot--audio { background: var(--social-orange); }
  .dot--photo { background: var(--social-blue); }
  .dot--video { background: var(--social-red); }

  .contacts {
    position: absolute; right: 21px; top: 153px;
    list-style: none; text-align: right;
  }
  .contacts li {
    height: 19.5px;
    font-size: 10.5px; color: var(--text-light);
    letter-spacing: 0.05em;
  }

  /* Back */
  .card--back .brand-name {
    left: 0; right: 0; top: 108px;
    text-align: center;
    font-size: 22px;
    color: var(--ink-black);
  }
  .tagline {
    position: absolute; left: 0; right: 0; top: 207px;
    text-align: center;
    font-size: 10px; letter-spacing: 0.06em;
    color: var(--ink-dark);
    text-transform: uppercase;
  }
</style>
</head>
<body>
<main class="canvas">
  <section class="card card--front">
    <div class="band-top"></div>
    <div class="band-bottom"></div>
    <div class="portrait" role="img" aria-label="Black and white portrait of the artist in a dark shirt"></div>
    <p class="brand-name">Copper Wave</p>
    <ul class="socials">
      <li>CopperWaveCW<span class="dot dot--audio"></span></li>
      <li>@therealcopperwavecw<span class="dot dot--photo"></span></li>
      <li>CopperWaveCW<span class="dot dot--video"></span></li>
    </ul>
    <ul class="contacts">
      <li>555-014-2231</li>
      <li>555-018-7740</li>
      <li>copperwavemania@example.com</li>
    </ul>
  </section>

  <section class="card card--back">
    <p class="brand-name">Copper Wave</p>
    <p class="tagline">Nothing worth having comes easy</p>
  </section>
</main>
</body>
</html>
```